Coral Ridge Pools New website

I currently operate a swimming pool service and repair business and looking for a re design for my website as it has been over 5 years since it was designed. current site is coralridgepoolsqx.com

```html
<!DOCTYPE html>
<html lang="en">
<head>
<meta charset="utf-8">
<title>Coral Ridge Pools</title>
<link href="https://fonts.googleapis.com/css2?family=Playfair+Display:wght@700;800&family=Poppins:wght@400;500;600;700&display=swap" rel="stylesheet">
<style>
:root{
  --navy:#0b5c9e;
  --orange:#f7931e;
  --ink:#333333;
  --soft:#f4f4f4;
  --stage:#9a9a9a;
  --dark:#26303a;
  --white:#ffffff;
}
*{box-sizing:border-box;margin:0;padding:0}
html,body{width:1200px;height:2445px;overflow:hidden;background:var(--stage)}
body{font-family:'Poppins',sans-serif;color:var(--ink);position:relative}
.page{position:absolute;left:81px;top:81px;width:1093px;height:2405px;background:var(--soft);transform:scale(.9497);transform-origin:0 0;box-shadow:0 4px 14px rgba(0,0,0,.35);overflow:hidden}
.abs{position:absolute}
.serif{font-family:'Playfair Display',serif}

/* hero */
.hero-art{position:absolute;left:0;top:0;width:1093px;height:640px}
.nav{position:absolute;top:6px;left:0;width:100%;display:flex;justify-content:center;gap:18px;font-size:13px;font-weight:600;color:var(--white)}
.nav a{color:inherit;text-decoration:none;padding-bottom:6px}
.nav a.active{border-bottom:2px solid var(--orange)}
.brand{position:absolute;top:120px;left:0;width:100%;text-align:center;font-family:'Playfair Display',serif;font-weight:700;font-size:36px;color:var(--white)}
.hero-title{position:absolute;top:268px;left:0;width:100%;text-align:center;font-family:'Playfair Display',serif;font-weight:700;font-size:44px;line-height:52px;color:var(--white);letter-spacing:.5px}
.hero-sub{position:absolute;top:383px;left:0;width:100%;text-align:center;font-size:24px;line-height:33px;color:var(--white)}
.btn{display:inline-block;background:var(--orange);color:var(--white);font-weight:700;text-transform:uppercase;border-radius:3px;text-align:center}
.hero-btn{position:absolute;left:456px;top:472px;width:181px;height:39px;line-height:39px;font-size:15px}
.mini-brand{position:absolute;top:628px;left:0;width:100%;text-align:center;font-family:'Playfair Display',serif;font-weight:700;font-size:15px;color:var(--navy)}

/* circle sign heading */
.sign{position:absolute;left:0;width:100%;display:flex;flex-direction:column;align-items:center}
.sign-row{display:flex;justify-content:center}
.sign-row span{display:inline-flex;align-items:center;justify-content:center;border-radius:50%;background:var(--navy);border:3px solid var(--orange);color:var(--white);font-family:'Playfair Display',serif;font-weight:700;margin:0 -2px}
.sign-row .gap{background:none;border:none}
.sign.lg span{width:48px;height:48px;font-size:36px}
.sign.md span{width:38px;height:38px;font-size:28px}

/* services */
.cards{position:absolute;top:830px;left:61px;display:flex;gap:26px}
.card{width:223px;height:255px;background:var(--white);border-radius:8px;text-align:center;padding-top:24px}
.card svg{display:block;margin:0 auto}
.card h3{font-family:'Playfair Display',serif;font-weight:700;font-size:17px;color:var(--navy);margin-top:14px}
.card p{font-size:10.5px;line-height:16px;color:var(--ink);margin:6px auto 0;width:190px}
.card .btn{margin-top:10px;font-size:9.5px;padding:0 10px;height:24px;line-height:24px}

/* about */
.about{position:absolute;top:1155px;left:0;width:1093px;height:375px}
.about svg{position:absolute;left:0;top:0}
.about-copy{position:absolute;left:635px;top:140px;width:415px;color:var(--white);font-size:10.5px;line-height:17px}
.about-copy p+p{margin-top:17px}
.about-copy .btn{margin-top:14px;font-size:9.5px;padding:0 10px;height:22px;line-height:22px}

/* cta */
.cta{position:absolute;top:1530px;left:0;width:1093px;height:245px;background:linear-gradient(90deg,#f5901a,#f89c2c 50%,#f5901a);text-align:center;color:var(--white)}
.cta h2{font-family:'Playfair Display',serif;font-weight:700;font-size:46px;margin-top:36px;line-height:56px}
.cta p{font-size:24px;margin-top:6px}
.cta .btn-navy{display:inline-block;margin-top:16px;width:235px;height:51px;line-height:51px;background:var(--navy);color:var(--white);font-weight:700;font-size:22px;border-radius:3px}

/* contact */
.contact-lead{position:absolute;top:1970px;left:0;width:100%;text-align:center;font-size:17px;line-height:23px;color:#444}
.form{position:absolute;left:174px;top:2038px;width:353px;height:250px;background:var(--white);border-radius:10px;padding:17px 19px}
.field{height:28px;border:1px solid #d8d8d8;border-radius:3px;font-size:8.5px;color:#999;padding:8px 8px;margin-bottom:9px}
.field.area{height:65px}
.send{display:inline-block;margin-top:3px;background:var(--orange);color:var(--white);font-size:9px;font-weight:600;height:23px;line-height:23px;padding:0 12px;border-radius:12px}
.touch{position:absolute;left:567px;top:2092px}
.touch h3{font-family:'Playfair Display',serif;font-weight:700;font-size:26px;color:var(--navy);margin-bottom:8px}
.touch li{list-style:none;display:flex;align-items:center;gap:8px;font-size:15px;color:var(--ink);height:29px}
.touch svg{flex:none}
.footer{position:absolute;top:2365px;left:0;width:100%;height:40px;background:var(--white);text-align:center;line-height:40px;font-size:10px;color:#444}
</style>
</head>
<body>
<div class="page">

  <svg class="hero-art" viewBox="0 0 1093 640" width="1093" height="640">
    <defs>
      <linearGradient id="heroSky" x1="0" y1="0" x2="0" y2="1">
        <stop offset="0" stop-color="#3a3550"/>
        <stop offset=".45" stop-color="#6a5560"/>
        <stop offset=".7" stop-color="#2c5f8f"/>
        <stop offset="1" stop-color="#1d6fb0"/>
      </linearGradient>
      <linearGradient id="heroSide" x1="0" y1="0" x2="1" y2="0">
        <stop offset="0" stop-color="#1e1a22" stop-opacity=".7"/>
        <stop offset=".5" stop-color="#000" stop-opacity="0"/>
        <stop offset="1" stop-color="#6b2d18" stop-opacity=".55"/>
      </linearGradient>
    </defs>
    <g role="img" aria-label="Rooftop pool between city towers at dusk with lounge chairs">
      <polygon points="0,0 1093,0 1093,505 546,612 0,505" fill="url(#heroSky)"/>
      <polygon points="0,0 1093,0 1093,505 546,612 0,505" fill="url(#heroSide)"/>
    </g>
    <polygon points="0,505 546,612 1093,505 1093,518 546,625 0,518" fill="#0b5c9e"/>
    <polygon points="0,518 546,625 1093,518 1093,530 546,637 0,530" fill="#f7931e"/>
  </svg>

  <nav class="nav">
    <a class="active" href="#">Home</a><a href="#">About</a><a href="#">Services</a><a href="#">Contact</a>
  </nav>
  <div class="brand">Coral Ridge Pools</div>
  <h1 class="hero-title">CRYSTAL CLEAR POOLS,<br>ALL YEAR ROUND</h1>
  <p class="hero-sub">Your trusted partner for pool maintenance,<br>repair &amp; remodeling in Las Vegas.</p>
  <a class="btn hero-btn" href="#">Get a Free Quote</a>
  <div class="mini-brand">Coral Ridge Pools</div>

  <div class="sign lg" style="top:705px">
    <div class="sign-row"><span>O</span><span>U</span><span>R</span></div>
    <div class="sign-row" style="margin-top:-1px"><span>S</span><span>E</span><span>V</span><span>I</span><span>C</span><span>E</span><span>S</span></div>
  </div>

  <div class="cards">
    <div class="card">
      <svg width="90" height="90" viewBox="0 0 90 90"><polygon points="45,3 87,45 45,87 3,45" fill="#fff" stroke="#0b5c9e" stroke-width="4"/><polygon points="45,11 79,45 45,79 11,45" fill="none" stroke="#f7931e" stroke-width="1.5"/></svg>
      <h3>Pool Cleaning</h3>
      <p>Regular cleaning to keep your pool sparkling clean &amp; hygienic for your family and friends.</p>
      <a class="btn" href="#">Learn More</a>
    </div>
    <div class="card">
      <svg width="90" height="90" viewBox="0 0 90 90"><polygon points="45,3 87,45 45,87 3,45" fill="#fff" stroke="#0b5c9e" stroke-width="4"/><polygon points="45,11 79,45 45,79 11,45" fill="none" stroke="#f7931e" stroke-width="1.5"/></svg>
      <h3>Repairs &amp; Equipment</h3>
      <p>From leak detection to pump &amp; filter repairs, our technicians fix issues promptly &amp; professionally.</p>
      <a class="btn" href="#">Learn More</a>
    </div>
    <div class="card">
      <svg width="90" height="90" viewBox="0 0 90 90"><polygon points="45,3 87,45 45,87 3,45" fill="#fff" stroke="#0b5c9e" stroke-width="4"/><polygon points="45,11 79,45 45,79 11,45" fill="none" stroke="#f7931e" stroke-width="1.5"/></svg>
      <h3>Maintenance Plans</h3>
      <p>Custom maintenance plans tailored to your needs for worry-free pool ownership.</p>
      <a class="btn" href="#">Learn More</a>
    </div>
    <div class="card">
      <svg width="90" height="90" viewBox="0 0 90 90"><polygon points="45,3 87,45 45,87 3,45" fill="#fff" stroke="#0b5c9e" stroke-width="4"/><polygon points="45,11 79,45 45,79 11,45" fill="none" stroke="#f7931e" stroke-width="1.5"/></svg>
      <h3>Renovation &amp; Remodel</h3>
      <p>Transform your backyard with custom pool resurfacing, tile work &amp; modern upgrades.</p>
      <a class="btn" href="#">Learn More</a>
    </div>
  </div>

  <section class="about">
    <svg width="1093" height="375" viewBox="0 0 1093 375">
      <defs>
        <linearGradient id="resort" x1="0" y1="0" x2="0" y2="1">
          <stop offset="0" stop-color="#7fb4dc"/>
          <stop offset=".5" stop-color="#6f8a5a"/>
          <stop offset=".75" stop-color="#4fb3d8"/>
          <stop offset="1" stop-color="#2f8cc4"/>
        </linearGradient>
      </defs>
      <rect width="1093" height="375" fill="#26303a"/>
      <polygon points="0,0 425,0 505,185 470,375 0,375" fill="url(#resort)" role="img" aria-label="Resort pool with palm trees and white gazebos"/>
      <polygon points="425,0 608,0 533,185 622,375 470,375 505,185" fill="#0b5c9e"/>
      <polyline points="608,0 533,185 622,375" fill="none" stroke="#f7931e" stroke-width="6"/>
    </svg>
    <div class="sign md" style="top:54px;left:635px;width:410px;align-items:flex-start">
      <div class="sign-row"><span>A</span><span>B</span><span>O</span><span>U</span><span>T</span><span class="gap"></span><span>C</span><span>O</span><span>R</span><span>A</span><span>L</span></div>
      <div class="sign-row"><span>R</span><span>I</span><span>D</span><span>G</span><span>E</span><span class="gap" style="width:10px"></span><span>P</span><span>O</span><span>O</span><span>L</span><span>S</span><span class="gap" style="width:10px"></span><span>L</span><span>V</span></div>
    </div>
    <div class="about-copy">
      <p>Coral Ridge Pools LV is a family-owned and operated pool service and repair company serving Las Vegas and surrounding areas. With over a decade of experience, we are dedicated to providing reliable, top-quality pool care so you can enjoy your backyard oasis year round.</p>
      <p>We take pride in our attention to detail, friendly customer service, and deep knowledge of pool systems. Whether you need weekly cleaning, urgent repairs or a complete pool renovation, our certified technicians are here to help.</p>
      <a class="btn" href="#">Learn More</a>
    </div>
  </section>

  <section class="cta">
    <h2>Relax, We’ve Got Your Pool Covered</h2>
    <p>Let our experts keep your pool safe, clean &amp; ready for every occasion.</p>
    <a class="btn-navy" href="#">Schedule Service</a>
  </section>

  <div class="sign lg" style="top:1857px">
    <div class="sign-row"><span>C</span><span>O</span><span>N</span><span>T</span><span>A</span><span>C</span><span>T</span></div>
    <div class="sign-row" style="margin-top:-4px"><span>U</span><span>S</span></div>
  </div>
  <p class="contact-lead">Ready to make a splash? Send us a message or give us a call<br>and we’ll get back to you as soon as possible.</p>

  <form class="form">
    <div class="field">Your Name</div>
    <div class="field">Email Address</div>
    <div class="field">Phone Number</div>
    <div class="field area">How can we help you?</div>
    <span class="send">Send Message</span>
  </form>

  <div class="touch">
    <h3>Get in Touch</h3>
    <ul>
      <li><svg width="22" height="22" viewBox="0 0 22 22"><circle cx="11" cy="11" r="10" fill="#fff" stroke="#f7931e" stroke-width="1.5"/><path d="M7.5 6.5l2 -.5 1.2 2.6-1.3 1c.6 1.3 1.6 2.3 2.9 2.9l1-1.3 2.6 1.2-.5 2c-4.6-.2-7.7-3.3-7.9-7.9z" fill="#0b5c9e"/></svg>(555) 014-2867</li>
      <li><svg width="22" height="22" viewBox="0 0 22 22"><circle cx="11" cy="11" r="10" fill="#fff" stroke="#f7931e" stroke-width="1.5"/><rect x="6" y="7.5" width="10" height="7" fill="none" stroke="#0b5c9e" stroke-width="1.4"/><path d="M6 7.5l5 4 5-4" fill="none" stroke="#0b5c9e" stroke-width="1.4"/></svg>info@coralridgepoolsqx.com</li>
      <li><svg width="22" height="22" viewBox="0 0 22 22"><circle cx="11" cy="11" r="10" fill="#fff" stroke="#f7931e" stroke-width="1.5"/><path d="M11 17s-4-4.2-4-7a4 4 0 0 1 8 0c0 2.8-4 7-4 7z" fill="#0b5c9e"/><circle cx="11" cy="10" r="1.4" fill="#fff"/></svg>Las Vegas, NV</li>
    </ul>
  </div>

  <footer class="footer">© 2026 Coral Ridge Pools LV. All rights reserved.</footer>
</div>
</body>
</html>
```